Speisekarten
Zielgruppe
Die Sola Brisa Kassel ist vorrangig in der hochwertigen Gastronomie und Hotellerie tätig. Unser Leitspruch: IMMER EINEN TICK MEHR ALS ERWARTET. MEHR QUALITÄT, MEHR VIELFALT, MEHR LEISTUNG, MEHR LEIDENSCHAFT IN JEDEM DETAIL.
Was dazu gehört: Eine vielseitige Genießerwelt, die ihresgleichen sucht: Zehn Event-Locations, drei Hotels, zwanzig Tagungsräume, sieben Restaurants, eine Eisbar, zwei Feinkostgeschäfte und einen eigenen Strandabschnitt an der Lahn dürfen wir zu uns zählen.
Ob tagen, erholen, feiern oder genießen, bei uns gibt es das Rundum-Paket.
Aufgabenstellung
Sehr hochwertiges Design einer Speisekarte für ein asiatisches Restaurant der Extraklasse.

```html
<!DOCTYPE html>
<html lang="de">
<head>
<meta charset="utf-8">
<title>Speisekarte – Sola Brisa Kassel</title>
<link rel="stylesheet" href="https://fonts.googleapis.com/css2?family=Encode+Sans+Semi+Condensed:wght@300;400&family=Kaushan+Script&family=Roboto+Slab:wght@500&display=swap">
<style>
  :root {
    --ink: #141414;
    --red: #e31b23;
    --red-deep: #a3271a;
    --cream: #f3e3c7;
    --sand: #c9a57a;
    --paper: #fbfaf7;
    --mist: #d9dcdf;
  }
  * { margin: 0; padding: 0; box-sizing: border-box; }
  html, body { width: 1200px; height: 849px; overflow: hidden; background: #fff; }
  .spread { position: relative; width: 1200px; height: 849px; display: flex; }

  /* Cover page */
  .cover { position: relative; width: 600px; height: 849px; overflow: hidden; }
  .cover-scene {
    position: absolute; inset: 0;
    background:
      radial-gradient(ellipse 62% 36% at 70% 78%, rgba(110,80,50,.55), rgba(110,80,50,0) 70%),
      radial-gradient(circle at 48% 46%, #ffffff 0%, #fbf3e6 32%, var(--cream) 48%, var(--sand) 60%, var(--red-deep) 78%, #8e1f15 100%);
  }
  .cover-glyph {
    position: absolute; left: 39px; top: 47px; width: 337px; height: 287px;
    background: radial-gradient(ellipse at 50% 50%, rgba(20,20,20,.85) 0%, rgba(20,20,20,.55) 45%, rgba(20,20,20,0) 72%);
  }
  .brand-mark {
    position: absolute; left: 65px; top: 226px; width: 40px; height: 120px;
    display: flex; flex-direction: column; align-items: center; justify-content: center;
    font-family: "Roboto Slab", serif; font-weight: 500; font-size: 25px; line-height: 27px;
    color: var(--red);
  }
  .cover-title {
    position: absolute; left: 104px; top: 336px;
    font-family: "Kaushan Script", cursive; font-size: 74px; line-height: 1;
    color: var(--red); transform: rotate(-4deg);
  }

  /* Menu page */
  .menu { position: relative; width: 600px; height: 849px; background: var(--paper); overflow: hidden; }
  .menu-scene {
    position: absolute; inset: 0;
    background:
      radial-gradient(ellipse 40% 30% at 90% 22%, rgba(170,176,184,.45), rgba(170,176,184,0) 70%),
      radial-gradient(ellipse 50% 30% at 30% 50%, rgba(180,184,190,.35), rgba(180,184,190,0) 70%),
      radial-gradient(ellipse 60% 30% at 60% 82%, rgba(160,165,172,.35), rgba(160,165,172,0) 70%),
      var(--paper);
  }
  .section-title {
    position: absolute; font-family: "Kaushan Script", cursive;
    font-size: 44px; line-height: 1; color: var(--red); transform: rotate(-4deg);
  }
  .dish { position: absolute; width: 452px; font-family: "Encode Sans Semi Condensed", sans-serif; color: var(--ink); }
  .dish-name { font-size: 21px; font-weight: 400; line-height: 24px; }
  .dish-text { font-size: 12.5px; font-weight: 300; line-height: 17px; margin-top: 4px; }
  .dish-price {
    position: absolute; width: 60px; text-align: right;
    font-family: "Encode Sans Semi Condensed", sans-serif; font-size: 21px; font-weight: 300; color: var(--ink);
  }
  .offer-stroke {
    position: absolute; left: 956px; top: 392px; width: 196px; height: 96px;
    background: var(--red); transform: rotate(-13deg); border-radius: 4px;
  }
  .offer-label {
    position: absolute; left: 990px; top: 398px; font-family: "Kaushan Script", cursive;
    font-size: 22px; line-height: 24px; color: var(--ink); transform: rotate(-14deg);
  }
</style>
</head>
<body>
<main class="spread">
  <section class="cover">
    <div class="cover-scene" role="img" aria-label="Illustration: Vollmond über nebliger Landschaft mit Pagode und kahlen Bäumen, rotbraun gerahmt"></div>
    <div class="cover-glyph" role="img" aria-label="Pinselkalligrafie des Zeichens für Wasser"></div>
    <div class="brand-mark"><span>N</span><span>A</span><span>M</span><span>I</span></div>
    <h1 class="cover-title">Speisekarte</h1>
  </section>

  <section class="menu">
    <div class="menu-scene" role="img" aria-label="Aquarell: Berge, Kirschblütenzweig, Pagode und Torii im Nebel"></div>
  </section>

  <h2 class="section-title" style="left:670px;top:44px;">Lorem ipsum</h2>

  <div class="dish" style="left:670px;top:129px;"><p class="dish-name">Lorem ipsum dolor sit amet</p><p class="dish-text">Lorem ipsum dolor sit amet, consectetuer adipiscing elit, sed diam nonummy nibh euismod tincidunt ut laoreet dolore magna aliquam erat volutpat.</p></div>
  <div class="dish-price" style="left:1062px;top:130px;">20€</div>

  <div class="dish" style="left:670px;top:208px;"><p class="dish-name">Lorem ipsum dolor sit amet</p><p class="dish-text">Lorem ipsum dolor sit amet, consectetuer adipiscing elit, sed diam nonummy nibh euismod tincidunt ut laoreet dolore magna aliquam erat volutpat.</p></div>
  <div class="dish-price" style="left:1062px;top:207px;">20€</div>

  <div class="dish" style="left:670px;top:295px;"><p class="dish-name">Lorem ipsum dolor sit amet</p><p class="dish-text">Lorem ipsum dolor sit amet, consectetuer adipiscing elit, sed diam nonummy nibh euismod tincidunt ut laoreet dolore magna aliquam erat volutpat.</p></div>
  <div class="dish-price" style="left:1062px;top:296px;">20€</div>

  <div class="offer-stroke" role="img" aria-label="Roter Pinselstrich"></div>
  <p class="offer-label">Angebot<br>&nbsp;&nbsp;&nbsp;des Tages:</p>

  <h2 class="section-title" style="left:674px;top:430px;">Lorem ipsum</h2>

  <div class="dish" style="left:674px;top:516px;"><p class="dish-name">Lorem ipsum dolor sit amet</p><p class="dish-text">Lorem ipsum dolor sit amet, consectetuer adipiscing elit, sed diam nonummy nibh euismod tincidunt ut laoreet dolore magna aliquam erat volutpat.</p></div>
  <div class="dish-price" style="left:1066px;top:517px;">20€</div>

  <div class="dish" style="left:674px;top:595px;"><p class="dish-name">Lorem ipsum dolor sit amet</p><p class="dish-text">Lorem ipsum dolor sit amet, consectetuer adipiscing elit, sed diam nonummy nibh euismod tincidunt ut laoreet dolore magna aliquam erat volutpat.</p></div>
  <div class="dish-price" style="left:1066px;top:594px;">20€</div>

  <div class="dish" style="left:674px;top:682px;"><p class="dish-name">Lorem ipsum dolor sit amet</p><p class="dish-text">Lorem ipsum dolor sit amet, consectetuer adipiscing elit, sed diam nonummy nibh euismod tincidunt ut laoreet dolore magna aliquam erat volutpat.</p></div>
  <div class="dish-price" style="left:1066px;top:683px;">20€</div>
</main>
</body>
</html>
```